Solace Chiropractic & Acupuncture Business Cards

I need a business card design that feels elevated. I am open to any of the logo designs uploaded. We have two doctors so I'll need to be able to change out the names.

Information:
Marnie Toller D.C., M.Ac. CTCM
584 W 12th St, Ste 320
Millbrook, OR 97419
solacegrove.net
541-555-0147
drmarnie@solacegrove.com
Updates

We have designs we like now, we are just trying to choose between top contenders. Thanks for your submissions!

Contact Information for Business Card

noted in description

Requirements
Must have
• ability to edit info if possible
Nice to have
• Please see our website solacegrove.net for our style and colors

```html
<!DOCTYPE html>
<html lang="en">
<head>
<meta charset="utf-8">
<title>Solace Chiropractic &amp; Acupuncture — Business Cards</title>
<link rel="stylesheet" href="https://fonts.googleapis.com/css2?family=Playfair+Display:wght@400&family=Open+Sans:wght@300;400&display=swap">
<style>
  :root {
    --page: #ffffff;
    --navy: #2b3346;
    --sand: #cdc3b6;
    --cream: #ebe6dd;
    --ink: #2f3648;
    --ink-soft: #4a5061;
    --seal: #9a9287;
  }
  * { margin: 0; padding: 0; box-sizing: border-box; }
  html, body {
    width: 1200px; height: 1000px; overflow: hidden;
    background: var(--page);
  }
  .canvas { position: relative; width: 1200px; height: 1000px; }

  .card {
    position: absolute; left: 281px; width: 640px; height: 359px;
  }
  .card--front { top: 106px; background: var(--navy); }
  .card--back  { top: 505px; background: var(--sand); }

  .wordmark {
    position: absolute; left: 0; right: 0; top: 134px;
    text-align: center; color: var(--cream);
    font-family: "Playfair Display", serif; font-weight: 400;
  }
  .wordmark__name { display: block; font-size: 72px; line-height: 1; letter-spacing: -1px; }
  .wordmark__tag  { display: block; margin-top: 6px; font-size: 11px; letter-spacing: 1px; text-transform: uppercase; }

  .doctor {
    position: absolute; left: 46px; top: 84px;
    font-family: "Playfair Display", serif; font-weight: 400;
    font-size: 40px; color: var(--ink); line-height: 1;
  }
  .credentials {
    position: absolute; left: 46px; top: 131px;
    font-family: "Open Sans", sans-serif; font-weight: 300;
    font-size: 19px; color: var(--ink);
  }
  .divider {
    position: absolute; left: 46px; top: 170px; width: 63px; height: 1px;
    background: var(--ink);
  }
  .contact {
    position: absolute; left: 46px; top: 196px; list-style: none;
    font-family: "Open Sans", sans-serif; font-weight: 400;
    font-size: 14px; letter-spacing: 0.3px; color: var(--ink-soft); line-height: 17px;
  }
  .contact__item { position: relative; padding-left: 32px; }
  .contact__item + .contact__item { margin-top: 13px; }
  .contact__item:nth-child(2) { margin-top: 5px; }
  .contact__icon {
    position: absolute; left: 0; top: 5px; width: 16px; height: 16px;
    fill: none; stroke: var(--ink); stroke-width: 1.2;
  }
  .contact__item--address .contact__icon { top: 9px; }

  .seal {
    position: absolute; left: 497px; top: 203px; width: 86px; height: 104px;
  }
  .seal__ring { fill: none; stroke: var(--seal); stroke-width: 0.8; }
  .seal__name {
    fill: var(--seal); font-family: "Playfair Display", serif; font-weight: 400; font-size: 15px;
  }
</style>
</head>
<body>
<main class="canvas">
  <section class="card card--front">
    <div class="wordmark">
      <span class="wordmark__name">Solace</span>
      <span class="wordmark__tag">Chiropractic &amp; Acupuncture</span>
    </div>
  </section>

  <section class="card card--back">
    <h1 class="doctor">Dr. Marnie Toller</h1>
    <p class="credentials">D.C., M.Ac. CTCM</p>
    <div class="divider"></div>
    <ul class="contact">
      <li class="contact__item contact__item--address">
        <svg class="contact__icon" viewBox="0 0 16 16"><path d="M8 15s-5-5.2-5-8.6A5 5 0 0 1 13 6.4C13 9.8 8 15 8 15z"/><circle cx="8" cy="6.4" r="1.8"/></svg>
        584 W 12th St, Ste 320<br>Millbrook, OR 97419
      </li>
      <li class="contact__item">
        <svg class="contact__icon" viewBox="0 0 16 16"><circle cx="8" cy="8" r="6.5"/><ellipse cx="8" cy="8" rx="3" ry="6.5"/><path d="M1.5 8h13M2.5 4.8h11M2.5 11.2h11"/></svg>
        solacegrove.net
      </li>
      <li class="contact__item">
        <svg class="contact__icon" viewBox="0 0 16 16"><path d="M3.2 1.8l2.3-.4 1.3 3-1.5 1.2a8 8 0 0 0 4.2 4.2l1.2-1.5 3 1.3-.4 2.3c-.2.8-1 1.3-1.8 1.2C6.8 12.5 3.5 9.2 2 4.5c-.2-.9.4-2.5 1.2-2.7z"/></svg>
        541-555-0147
      </li>
      <li class="contact__item">
        <svg class="contact__icon" viewBox="0 0 16 16"><rect x="1" y="3" width="14" height="10"/><path d="M1 3l7 5.5L15 3M1 13l5-4.5M15 13l-5-4.5"/></svg>
        drmarnie@solacegrove.com
      </li>
    </ul>
    <svg class="seal" viewBox="0 0 86 104">
      <ellipse class="seal__ring" cx="43" cy="52" rx="42" ry="51"/>
      <text class="seal__name" x="43" y="57" text-anchor="middle">Solace</text>
    </svg>
  </section>
</main>
</body>
</html>
```